Sharp, new and modern business flyer

We are an industrial crate manufacturer whose core customer base is in the aeronautical parts sector. We also however build very custom travel show crates and road cases for any spectrum of industries. We have a substantial facility and can accommodate large, production orders so we would like to attract large, local businesses if possible, but ship crates nationwide as well. We have an old tri fold flyer that we have been using for over 3+ years that I will attach for reference but it desperately needs a fresh new look and complete revamp! Our slogan is "Innovative Crating With Superior Service." We are known in the industry as being extremely fast as well as providing excellent customer service and crate design work. We have also in the last year, added two globes to the background of our logo. I am attaching our current business cards that show how we incorporate that. Feel free to visit our website as well as our Chatterloop page for more info and current pictures. Both are Marlowbeckindustries.com.

Target Market(s)

Mid to large local business and corporations. Industrial and manufacturing - especially aeronautical or medical (delicate surgical equipment) as well as military.

Industry/Entity Type

Manufacturer

Font styles to use
Sans Serif
Other font styles liked:
• Stencil

Colors

Designer to choose colors to be used in the design.

Requirements
Must have
• 1. Current photos and descriptions of our capabilities. Our most current products are on our Chatterloop page and our capabilities are on our website.
• 2. Our flyer must state that "All of our quality products are built with lumber that is ISPM 15 Heat Treatment Certified"
• 3. Please add custom pallets as well as on-site crating
Nice to have
• A new, modern look that shows us as current and growing.
Should not have
• Woman owned listed...we are no longer woman owned.

```html
<!DOCTYPE html>
<html lang="en">
<head>
<meta charset="utf-8">
<title>Marlowbeck Industries – Tri-fold Brochure</title>
<link href="https://fonts.googleapis.com/css2?family=Oswald:wght@500;700&family=Open+Sans:wght@400;600;700&display=swap" rel="stylesheet">
<style>
  :root{
    --ink:#2a2a2a;
    --ink-deep:#1f1f1f;
    --yellow:#f3b21a;
    --paper:#ffffff;
    --grey:#d6d6d6;
    --text:#3a3a3a;
    --wood:#b08a5a;
    --wood-dark:#6e5236;
  }
  *{box-sizing:border-box;margin:0;padding:0}
  html,body{width:804px;height:1200px;overflow:hidden;background:#fff}
  body{position:relative;font-family:"Open Sans",Arial,sans-serif;color:var(--text)}
  .sheet{position:absolute;left:13px;width:778px;background:var(--paper);box-shadow:0 2px 6px rgba(0,0,0,.25);overflow:hidden}
  .sheet--outside{top:6px;height:516px}
  .sheet--inside{top:549px;height:626px}
  .panel{position:absolute;top:0;height:100%;width:259px;overflow:hidden}
  .panel--1{left:0}.panel--2{left:259px}.panel--3{left:519px}
  .dark{background:var(--ink);color:#fff}
  .photo{position:absolute;background:linear-gradient(135deg,var(--wood) 0%,var(--wood-dark) 100%)}
  .photo--grey{background:linear-gradient(135deg,#9a9a9a,#4a4a4a)}
  .head{font-family:"Oswald",Arial,sans-serif;font-weight:700;text-transform:uppercase;color:var(--yellow);letter-spacing:.3px}
  .copy{font-size:7.6px;line-height:1.45}
  .abs{position:absolute}
  .logo{position:absolute;width:62px;height:62px;background:var(--yellow);display:flex;align-items:center;justify-content:center;font-family:"Oswald",Arial,sans-serif;font-weight:700;font-size:10px;color:var(--ink);text-transform:uppercase}
  .bullets{list-style:none}
  .bullets li{position:relative;padding-left:10px;margin-bottom:7px}
  .bullets li::before{content:"";position:absolute;left:0;top:3px;width:5px;height:5px;background:var(--yellow)}
  .services{list-style:none;font-size:8.6px;line-height:1.55;color:#fff}
  .services li{padding-left:11px;position:relative}
  .services li::before{content:"";position:absolute;left:0;top:5px;width:5px;height:5px;background:var(--yellow)}
  .ship{font-family:"Oswald",Arial,sans-serif;font-weight:700;font-size:10px;line-height:1.15;color:var(--yellow);text-transform:uppercase}
  .web{font-family:"Oswald",Arial,sans-serif;font-weight:700;font-size:10px;color:var(--ink)}
  .band{position:absolute;background:var(--ink);display:flex;align-items:center;padding:0 14px}
  .band .head{font-size:12px;line-height:1.2}
  .grid{position:absolute;display:grid;grid-template-columns:repeat(3,1fr);gap:5px}
  .grid .cell{height:46px;background:linear-gradient(135deg,var(--wood),var(--wood-dark))}
</style>
</head>
<body>

<!-- Outside spread -->
<section class="sheet sheet--outside">

  <article class="panel panel--1">
    <div class="photo" style="left:0;top:0;width:259px;height:186px" role="img" aria-label="Photo of stacked wooden shipping crates in the facility"></div>
    <svg class="abs" style="left:0;top:0" width="259" height="186"><polygon points="200,0 259,0 259,60" fill="#f3b21a"/><polygon points="0,150 0,186 60,186" fill="#2a2a2a"/></svg>
    <h2 class="head abs" style="left:16px;top:198px;font-size:14px;border-left:4px solid var(--yellow);padding-left:7px">About Us</h2>
    <p class="copy abs" style="left:16px;top:224px;width:228px">Our services include shipping crates, military crates, road cases, heavy equipment crating and rugged corrugated cardboard boxes. Beginning with on-site design and consulting services, we suggest ways to improve a company's performance. Our brand new enlarged modern facility and experienced staff provide fast delivery of all sizes and quantities of quality products.</p>
    <p class="copy abs" style="left:16px;top:318px;width:228px">All of our quality products are built with lumber that is ISPM 15 Heat Treatment Certified, ready for international shipping.</p>
    <div class="abs" style="left:16px;top:384px;width:130px;height:72px;background:var(--grey)" role="img" aria-label="Map of the United States"></div>
    <p class="ship abs" style="left:156px;top:398px;width:90px">We ship<br>anywhere<br>in the U.S.A</p>
    <svg class="abs" style="left:0;top:486px" width="259" height="30"><rect width="259" height="30" fill="#2a2a2a"/><polygon points="150,0 259,0 259,30 180,30" fill="#f3b21a"/></svg>
  </article>

  <article class="panel panel--2 dark">
    <h2 class="head abs" style="left:0;top:14px;width:259px;text-align:center;font-size:11.5px;line-height:1.2">Innovative Crating<br>with Superior Service</h2>
    <ul class="bullets copy abs" style="left:18px;top:52px;width:226px">
      <li>Perfect for shipping or for storage, our corrugated boxes are available in single, double or triple wall construction.</li>
      <li>In response to many requests, we are excited to present our newest product line: custom designed cardboard boxes built to fit your parts.</li>
      <li>We provide solutions for any product line or the custom road case. All road cases are built to your specifications with many options in hardware and foam.</li>
      <li>We specialize in fragile, high value cargo with custom designed solutions.</li>
      <li>We install hinges, hasps, handles, lamps, casters, dividers and foam for the perfect fit.</li>
    </ul>
    <p class="abs" style="left:0;top:330px;width:259px;text-align:center;font-size:8px;font-weight:700;color:var(--yellow)">Please call us with any crating questions<br>that you may have.</p>
    <div class="abs" style="left:0;top:360px;width:259px;height:156px;background:var(--paper)"></div>
    <div class="logo" style="left:98px;top:372px">MB</div>
    <p class="abs" style="left:0;top:442px;width:259px;text-align:center;font-size:7.5px;color:var(--text)">To request a quote please call us</p>
    <p class="abs" style="left:0;top:454px;width:259px;text-align:center;font-family:'Oswald',Arial,sans-serif;font-weight:700;font-size:12px;color:var(--ink)">(555) 214-0637</p>
    <p class="abs" style="left:0;top:476px;width:259px;text-align:center;font-size:7.2px;color:var(--text)">service@marlowbeckindustries.com<br>Marlowbeckindustries.com</p>
  </article>

  <article class="panel panel--3">
    <div class="photo" style="left:0;top:0;width:259px;height:262px" role="img" aria-label="Photo of a large open wooden crate being built in the warehouse"></div>
    <div class="logo" style="left:185px;top:12px;transform:rotate(0deg)">MB</div>
    <div class="photo photo--grey" style="left:0;top:262px;width:259px;height:108px" role="img" aria-label="Photo of work gloves and a forklift moving crates"></div>
    <div class="band" style="left:0;top:370px;width:259px;height:72px"><h2 class="head" style="font-size:12px;line-height:1.25;text-align:right;width:100%">We solve customer's<br>product crating and<br>storage problems!</h2></div>
    <p class="web abs" style="left:0;top:470px;width:259px;text-align:right;padding-right:18px">www.Marlowbeckindustries.com</p>
  </article>
</section>

<!-- Inside spread -->
<section class="sheet sheet--inside">

  <article class="panel panel--1 dark">
    <h2 class="head abs" style="left:18px;top:18px;width:225px;font-size:13px;line-height:1.2">Our quality products and<br>services include:</h2>
    <ul class="services abs" style="left:18px;top:62px;width:225px">
      <li>Crates</li><li>Production Crates</li><li>Military Crates</li><li>Custom Corrugated Cardboard Boxes</li><li>Road Cases</li><li>Heavy Equipment Skidding &amp; Crating</li><li>Trade Show Crates &amp; Cases</li><li>Composite Crates</li><li>Stretch &amp; Shrink Wrapping</li><li>Shock Control Systems</li><li>International Wood Pallets</li><li>Custom Pallets &amp; On-Site Crating</li>
    </ul>
    <div class="photo" style="left:18px;top:298px;width:223px;height:210px" role="img" aria-label="Photo of a tall stack of finished wooden crates"></div>
    <div class="abs" style="left:18px;top:528px;width:110px;height:64px;background:#555" role="img" aria-label="Map of the United States"></div>
    <p class="ship abs" style="left:138px;top:538px;width:105px">We ship<br>anywhere<br>in the USA</p>
  </article>

  <article class="panel panel--2">
    <div class="abs dark" style="left:0;top:0;width:259px;height:42px"></div>
    <h2 class="head abs" style="left:16px;top:12px;font-size:14px">Production Crates</h2>
    <p class="copy abs" style="left:16px;top:56px;width:228px">If you plan repeat orders for crates of consistent size and shape, we can give you the value of lower production techniques, and will offer personalized service to your project.</p>
    <p class="copy abs" style="left:16px;top:112px;width:228px">Our production crating options allow us to streamline raw material procurement and schedule the assembly of multiples, maximizing efficiencies in your cost.</p>
    <p class="copy abs" style="left:16px;top:166px;width:228px">Our careful attention to your production schedule allows us to meet tight deadlines quickly, without long lead times.</p>
    <p class="copy abs" style="left:16px;top:210px;width:228px">Production crate savings can be applied to all of our various product lines.</p>
    <div class="photo photo--grey" style="left:16px;top:246px;width:228px;height:116px" role="img" aria-label="Photo of a forklift carrying crates inside the facility"></div>
  </article>

  <article class="panel panel--3">
    <div class="photo" style="left:0;top:0;width:259px;height:150px" role="img" aria-label="Photo of wooden crates ready for shipping"></div>
    <div class="logo" style="left:180px;top:126px">MB</div>
    <div class="grid" style="left:14px;top:420px;width:231px">
      <div class="cell" role="img" aria-label="Photo of a custom crate"></div>
      <div class="cell" role="img" aria-label="Photo of a road case"></div>
      <div class="cell" role="img" aria-label="Photo of a pallet"></div>
      <div class="cell" role="img" aria-label="Photo of a military crate"></div>
      <div class="cell" role="img" aria-label="Photo of a trade show crate"></div>
      <div class="cell" role="img" aria-label="Photo of crated equipment"></div>
    </div>
    <p class="web abs" style="left:0;top:596px;width:259px;text-align:right;padding-right:18px">www.Marlowbeckindustries.com</p>
  </article>

  <div class="band" style="left:259px;top:372px;width:470px;height:38px"><h2 class="head" style="font-size:12.5px">We solve customer's product crating<br>and storage problems!</h2></div>
</section>

</body>
</html>
```